Word Doc Design for construction report

We have a database that dumps all of this data into this word doc. We need a much more appealing, visually friendly document. I have attached the main document and the cover page.
You don't need to edited all the repeated pages, just give us a style guide. I have attached our branding.
Updates

Hi I have pulled together a final design and now just need someone to put it all into a word doc. The final document is 36 pages. I am prepared to pay the design fee listed plus a $200 tip, however, we need it delivered by Monday. Is there anyone available to do this work?

Requirements
Must have
• Be easy on the eye as there is a LOT of repeated content

```html
<!DOCTYPE html>
<html lang="en">
<head>
<meta charset="utf-8">
<title>ACT Maintenance Plan – Style Guide Pages</title>
<link href="https://fonts.googleapis.com/css2?family=Montserrat:wght@300;400;500;600;700&display=swap" rel="stylesheet">
<style>
:root{
  --teal:#1aa99c;
  --blue:#2298d6;
  --navy:#1d3b66;
  --ink:#2b2b2b;
  --grey:#6d6d6d;
  --rule:#d4d4d4;
  --shade:#f1f1f1;
  --bg:#ffffff;
}
*{box-sizing:border-box;margin:0;padding:0}
html,body{width:789px;height:1200px;overflow:hidden;background:var(--bg)}
body{position:relative;font-family:"Montserrat",sans-serif;color:var(--ink)}
.page{position:absolute;background:#fff;box-shadow:2px 3px 6px rgba(0,0,0,.35);overflow:hidden;font-size:3px;line-height:1.35}
.footer{position:absolute;right:8px;bottom:4px;text-align:right;font-size:2.2px;color:var(--grey)}
.footer .num{color:var(--blue);font-size:2.8px;display:block}
.h-blue{color:var(--blue);font-weight:600}
.h-teal{color:var(--teal);font-weight:600}
p{margin-bottom:2.5px;text-align:justify}

/* cover */
.cover{left:37px;top:34px;width:215px;height:305px}
.brand{position:absolute;top:24px;left:0;width:100%;display:flex;justify-content:center;align-items:center;gap:4px;color:var(--navy)}
.brand .mark{width:8px;height:8px;background:var(--navy)}
.brand .name{font-size:9px;font-weight:500;line-height:1}
.cover-photo{position:absolute;left:0;top:56px;width:150px;height:190px;background:linear-gradient(180deg,#5f86b8 0%,#8fb0d3 30%,#d9c7a8 55%,#5a4a30 78%,#1f2a1c 100%)}
.title-box{position:absolute;left:88px;top:56px;width:127px;height:76px;background:var(--blue);color:#fff;padding:8px 10px}
.title-box h1{font-size:14px;font-weight:600;line-height:1.25}
.title-box .date{font-size:5.5px;margin-top:5px;font-weight:500}
.title-box .line{position:absolute;left:0;right:0;bottom:0;height:1px;background:#fff;opacity:.6}
.cover-address{position:absolute;left:13px;top:257px;font-size:5.5px;line-height:1.4;color:var(--ink)}
.contact-box{position:absolute;left:123px;top:235px;width:92px;height:70px;background:var(--teal);color:#fff;text-align:right;padding:10px 8px;font-size:4px;line-height:1.35}
.contact-box .gap{height:4px}

/* page 2 */
.summary{left:294px;top:34px;width:215px;height:305px;padding:14px 15px 0 17px}
.summary h2{font-size:5px;font-weight:500;display:flex;align-items:center;gap:4px;margin-bottom:4px}
.summary h2::after{content:"";flex:1;height:.5px;background:var(--ink)}
.kv{width:100%;border-collapse:collapse;margin-bottom:5px}
.kv td{font-size:3px;height:5.2px;padding:0 2px;border-bottom:.4px solid #fff}
.kv td.k{background:var(--teal);color:#fff;width:68px}
.kv td.v{background:var(--shade)}
.summary ul{margin:0 0 2px 12px;font-size:3px}
.important{border-left:1.5px solid var(--blue);padding-left:4px;margin:3px 0;font-style:italic;font-size:2.8px}
.important b{color:var(--blue);font-weight:500}
.sig{margin:6px 0 0 10px;width:50px;height:10px}
.signame{margin-left:18px;font-size:3px;font-weight:600;text-align:center;width:44px}

/* page 3 */
.links{left:536px;top:34px;width:215px;height:305px;padding:0 15px}
.badges{display:flex;justify-content:space-around;align-items:center;margin-top:36px;height:24px}
.badge{background:#e4e7ea}
.badge.b1{width:18px;height:20px}
.badge.b2{width:46px;height:18px;border-radius:9px}
.badge.b3{width:48px;height:20px}
.note{background:var(--shade);text-align:center;font-style:italic;font-size:2.6px;padding:2px 10px;margin-top:4px}
.map{position:absolute;left:15px;width:181px}
.map.street{top:98px;height:94px;background:linear-gradient(135deg,#cfe8c6 0%,#e9efe4 40%,#a9cfe9 70%,#d7ebcc 100%)}
.map.aerial{top:196px;height:105px;background:linear-gradient(160deg,#55604d 0%,#7d8574 40%,#5c6a7b 70%,#3f4a3a 100%)}

/* shared table */
.tbl{width:100%;border-collapse:collapse}
.tbl th{background:var(--teal);color:#fff;font-weight:500;text-align:left;font-size:2.8px;padding:.6px 2px}
.tbl td{font-size:2.6px;padding:.5px 2px;border-bottom:.4px solid var(--ink);line-height:1.2;vertical-align:middle}
.tbl td.area{background:var(--shade);border-bottom:.4px solid #fff}

/* page 4 */
.observe{left:74px;top:378px;width:293px;height:207px;padding:16px 13px 0 12px}
.observe h3{font-size:6px;margin-bottom:1px}
.observe .lead{font-size:2.6px;margin-bottom:4px;line-height:1.25}
.observe .tbl td{height:6.3px}

/* page 5 */
.action{left:427px;top:378px;width:291px;height:207px;padding:20px 12px 0 13px}
.action h3{font-size:6.5px}
.action .lead{font-size:2.6px;margin-bottom:6px}
.action .tbl td{height:6.5px;border-bottom:none;text-align:center}
.action .tbl td:first-child{background:var(--shade);text-align:left;border-bottom:.4px solid #fff}
.action .tbl th{text-align:center}
.action .tbl th:first-child{text-align:left}

/* page 6 */
.esl{left:74px;top:608px;width:293px;height:206px;padding:20px 7px 0 7px}
.esl .lead{font-size:2.8px;margin-bottom:4px}
.grid-head,.grid-row{display:grid;grid-template-columns:72px 20px repeat(16,12px)}
.grid-head{background:var(--teal);color:#fff;font-size:2.6px;height:6px;align-items:center;text-align:center}
.grid-row{height:7.7px;align-items:center;font-size:2.6px;border-bottom:.4px solid var(--ink);background-image:repeating-linear-gradient(90deg,transparent 0 11.6px,#555 11.6px 12px);background-position:92px 0;background-repeat:no-repeat;background-size:192px 100%}
.grid-row span.lbl{grid-column:1;line-height:1.05;padding-right:2px;border-right:.4px solid #555;height:100%;display:flex;align-items:center}
.grid-row span.yrs{grid-column:2;text-align:center;line-height:1.05}
.grid-row .tick{width:3.2px;height:3.2px;border:.4px solid var(--teal);justify-self:center;position:relative}
.grid-row .tick::after{content:"";position:absolute;left:.7px;top:.3px;width:1px;height:1.8px;border:solid var(--teal);border-width:0 .4px .4px 0;transform:rotate(45deg)}
.grid-row .yr-text{font-size:2.6px;justify-self:center}
.grid-section{font-size:2.8px;height:6px;display:flex;align-items:flex-end;border-bottom:.4px solid var(--ink)}

/* page 7 */
.plan{left:427px;top:608px;width:291px;height:206px;padding:20px 12px 0 13px}
.plan h3{font-size:9px;color:var(--blue);font-weight:500;margin-bottom:5px}
.band{background:var(--blue);color:#fff;font-size:5px;padding:1.5px 4px;font-weight:500;margin-bottom:2px}
.band.teal{background:var(--teal)}
.types td{font-size:2.6px;padding:1.2px 4px;border-bottom:.4px solid var(--ink);vertical-align:top}
.types td:first-child{width:44px}
.meta{display:flex;justify-content:space-between;font-size:3px;margin-top:1px}
.meta b{font-weight:600;font-style:italic;color:var(--ink)}
.nextdate{color:#e45c4a;font-style:italic;font-size:3px;margin-bottom:4px}
.wp-row{display:flex;font-size:2.6px;gap:0;align-items:center}
.wp-row .lab{width:55px;font-weight:600}
.wp-row .y{width:12.7px;text-align:center}
.wp-note{font-size:1.8px;font-style:italic;margin:1px 0 2px}
.history td{font-size:2.6px;padding:1px 4px}
.history tr.head td{background:var(--shade);font-weight:600}

/* pages 8–9 */
.scope{left:153px;top:854px;width:216px;height:303px;padding:14px 14px 0 15px}
.terms{left:424px;top:854px;width:214px;height:303px;padding:14px 14px 0 14px}
.scope h3{font-size:5.5px;font-weight:400;margin-bottom:4px}
.scope h4,.terms h4{font-size:3px;color:var(--teal);font-weight:500;margin-top:2px}
.scope p,.terms p{font-size:2.6px;line-height:1.3}
.terms h3{font-size:5px;color:var(--teal);font-weight:400;margin:3px 0 2px}
.access{width:100%;border-collapse:collapse;margin:3px 0}
.access th{background:var(--teal);color:#fff;font-size:2.6px;font-weight:500;font-style:italic;padding:1.5px}
.access td{font-size:2.6px;text-align:center;padding:1.5px;border-bottom:.4px solid var(--rule);font-style:italic}
.terms ul{margin-left:8px;font-size:2.6px}
</style>
</head>
<body>

<!-- Cover -->
<section class="page cover">
  <div class="brand">
    <span class="mark"></span>
    <span class="name">Homestead Reports</span>
  </div>
  <div class="cover-photo" role="img" aria-label="Photograph of a multi-storey apartment building at dusk with trees in front"></div>
  <div class="title-box">
    <h1>ACT<br>Maintenance<br>Plan</h1>
    <div class="date">2 May 2022</div>
    <div class="line"></div>
  </div>
  <div class="cover-address">UNITS PLAN1722<br>2 SAMPLE STREET CANBERRA CITY</div>
  <div class="contact-box">
    homesteadreports.com.au<br>hello@homesteadreports.com.au
    <div class="gap"></div>
    18 Warrick Lane<br>Ashvale ACT 2690<br>p 6200 0199
  </div>
</section>

<!-- Report summary -->
<section class="page summary">
  <h2>REPORT SUMMARY</h2>
  <table class="kv">
    <tr><td class="k">CLIENT</td><td class="v">Keystone Strata Group Pty Ltd</td></tr>
    <tr><td class="k">BUILDING LOCATION</td><td class="v">2 Sample Street Canberra City ACT</td></tr>
    <tr><td class="k">BLOCK NUMBER</td><td class="v">13</td></tr>
    <tr><td class="k">SECTION NUMBER</td><td class="v">12</td></tr>
    <tr><td class="k">SCHEME NUMBER</td><td class="v">UP1722</td></tr>
  </table>
  <table class="kv">
    <tr><td class="k">INSPECTION DATE</td><td class="v">2 May 2022</td></tr>
    <tr><td class="k">INSPECTOR</td><td class="v">Liam Torrent</td></tr>
    <tr><td class="k">WEATHER CONDITIONS</td><td class="v">Fine</td></tr>
    <tr><td class="k">REFERENCE NUMBER</td><td class="v">35TST</td></tr>
  </table>
  <div class="h-blue">Project Scope</div>
  <p>This Maintenance Plan has been compiled to assist the Owners Corporation and Strata Managers to meet their obligations with respect to the following legislation (both as amended 1 November 2020):</p>
  <ul><li>Unit Titles (Management) Act 2011 (s24);</li><li>Unit Titles (Management) Regulation 2011 (s4A)</li></ul>
  <div class="h-blue">Building Class</div>
  <ul><li>Residential Units are Class A</li></ul>
  <p>In typical Class A Units Plans, the unit owner owns the inside of the unit but not the main structure of the building. Usually, the individual owner owns from the inside of their lot to halfway out through the boundary walls, ceiling and the floor. In general, the Owners Corporation owns the walls, ceiling and floor from outside of the lot to halfway in. Floor coverings, light fittings and curtains are all the property of the unit owner.</p>
  <p>The Unit Titles (Management) Act 2011 and associated regulations provide the framework for the management of multi-unit residential properties. All Owners Corporations are required to hold a Maintenance Plan. The Executive Committee then references this plan as part of their responsibility for overseeing the maintenance of the common property, including copies of manuals and warranties where available.</p>
  <p>Following the preparation of our project file for 2 Sample Street Canberra which included referencing materials such as maintenance schedules, sinking fund reports, warranties and manufacturer's recommendations, our Building Inspector conducted a comprehensive on-site visual inspection on 2 May 2022. It is critical that this Maintenance Plan is monitored and updated on an ongoing basis to ensure the optimum working condition of systems, equipment and structures.</p>
  <div class="important"><b>IMPORTANT:</b> This report is intended to be read in its entirety. It has been commissioned to satisfy the requirements of a Maintenance Plan under the Act. The appropriate Strata Group Representative or Members of the Body Corporate Executive are requested to contact our company if any content is not fully understood.</div>
  <div class="h-blue" style="font-style:italic;font-size:2.8px">Please refer to Important Scope and Limitations at the end of this document.</div>
  <p style="margin-top:2px">Thank you for the opportunity to work with you on this project, please do not hesitate to contact our team.</p>
  <svg class="sig" viewBox="0 0 50 10" aria-hidden="true"><path d="M2 8 Q8 1 12 6 T22 5 L30 6 Q38 4 48 6" fill="none" stroke="#555" stroke-width=".5"/></svg>
  <div class="signame">Liam Torrent<br>Senior Building Inspector</div>
  <div class="footer"><span class="num">Page | 2</span>2 Sample Street Canberra City · COPYRIGHT: Homestead Reports</div>
</section>

<!-- Partners and maps -->
<section class="page links">
  <div class="badges">
    <div class="badge b1"></div>
    <div class="badge b2"></div>
    <div class="badge b3"></div>
  </div>
  <div class="note">A percentage from every inspection contributes to our inhouse charity, supporting those in our community who do not have a place to call home. Visit our website to learn more.</div>
  <p style="font-size:2.8px;margin-top:6px">A comprehensive photo log of all photographs and documents captured during the maintenance plan inspection on 2 May 2022 have been supplied with this report.</p>
  <div class="map street" role="img" aria-label="Street map of central Canberra with the site circled"></div>
  <div class="map aerial" role="img" aria-label="Aerial photograph of the city block with the building circled"></div>
  <div class="footer"><span class="num">3</span></div>
</section>

<!-- General observations -->
<section class="page observe">
  <h3 class="h-teal">General observations summary</h3>
  <p class="lead">The preparation of this Maintenance Plan included a comprehensive on-site inspection where building elements noted in the plan were reviewed to determine life cycles and continuity of service. Whilst the purpose of a maintenance plan is not to specifically address defects, any observations noted have been provided below as a courtesy. <b><i>Please refer to our Scope &amp; Limitations at the end of this document.</i></b></p>
  <table class="tbl">
    <tr><th style="width:42px">Area</th><th style="width:46px">Observation</th><th>Details</th></tr>
    <tr><td class="area" rowspan="6">Superstructure</td><td>Maintenance</td><td>Exterior of building adjacent to gymnasium requires painting</td></tr>
    <tr><td>Maintenance</td><td>Exterior of building adjacent to guest recreation room requires repainting</td></tr>
    <tr><td>Observation</td><td>Dutch paint observed in basement, clearly used for some external surfaces, but not a full building repaint</td></tr>
    <tr><td>Maintenance</td><td>Flaking paint was observed to balcony ceilings below the old pool area</td></tr>
    <tr><td>Maintenance</td><td>The window sill to a window adjacent to the outdoor recreation areas has deteriorated and requires repairs or replacement</td></tr>
    <tr><td>Maintenance</td><td>Some areas of foyer floor tiling require grout repairs</td></tr>
    <tr><td class="area">Garage Door</td><td>Observation</td><td>Observed servicemen at the building during our inspection</td></tr>
    <tr><td class="area">Basement line marking</td><td>Observation</td><td>There is varying levels of deterioration of lines, touch-ups to some areas is advised</td></tr>
    <tr><td class="area">Rooftop recreation area adjacent to tennis court</td><td>Landscaping</td><td>Rooftop recreation area requires weeding/spraying</td></tr>
    <tr><td class="area">Outdoor furniture</td><td>Maintenance/Replacement</td><td>Outdoor furniture adjacent to tennis court generally affected by weather. Serviceable. Would recommend outdoor cover if replaced.</td></tr>
    <tr><td class="area">Gym and public washrooms</td><td>Maintenance</td><td>There are some damaged ceiling tiles</td></tr>
    <tr><td class="area">Hallways</td><td>Maintenance</td><td>Patch painting, scuffing and impact damage was noted to some areas</td></tr>
    <tr><td class="area">Recreation room</td><td>Maintenance</td><td>Paint bubbing on some walls</td></tr>
    <tr><td class="area">Recreation room</td><td>Maintenance</td><td>The door handle to the recreation room is loose and requires repairs</td></tr>
    <tr><td class="area">Cooling tower</td><td>Maintenance</td><td>There is efflorescence present to a condenser pump from water leakage</td></tr>
    <tr><td class="area">Recreation deck</td><td>Structural defect/Hazard</td><td>The timber deck requires repairs and is structurally unsound</td></tr>
    <tr><td class="area">Stairwell</td><td>Maintenance</td><td>There are chipped and cracked tiles to the stairwell in some areas</td></tr>
    <tr><td class="area">Washroom</td><td>Maintenance</td><td>There are some damaged ceiling tiles</td></tr>
    <tr><td class="area">Sewer pump</td><td>Maintenance</td><td>Backflow prevention last tested 2014</td></tr>
    <tr><td class="area">Tennis court</td><td>Maintenance</td><td>Water was holding to areas of the court surface, drainage maintenance is recommended</td></tr>
  </table>
  <div class="footer"><span class="num">Page | 4</span>2 Sample Street Canberra City · COPYRIGHT: Homestead Reports</div>
</section>

<!-- Next action plan -->
<section class="page action">
  <h3 class="h-blue">Next Action Plan</h3>
  <p class="lead">To assist with future planning, inspections recommended over the next 18 months are detailed below:</p>
  <table class="tbl">
    <tr><th style="width:88px">Building Element</th><th style="width:44px">Type</th><th style="width:58px">Last Inspector</th><th>Next Inspection Due</th></tr>
    <tr><td>Superstructure</td><td>Routine</td><td>Homestead Reports</td><td>May 2023</td></tr>
    <tr><td>Basement/Car Accommodation</td><td>Routine</td><td>Homestead Reports</td><td>May 2023</td></tr>
    <tr><td>Cleaning/Sanitation</td><td>Sanitation</td><td>Cleanline</td><td></td></tr>
    <tr><td>Driveways, Pathways &amp; Parking</td><td>Routine</td><td>Homestead Reports</td><td>May 2023</td></tr>
    <tr><td>Electrical &amp; Security</td><td>Operational</td><td>Voltcare</td><td></td></tr>
    <tr><td>External Works</td><td>Routine</td><td>Homestead Reports</td><td>May 2023</td></tr>
    <tr><td>Fire Protection Systems &amp; Evacuation</td><td>Routine/Safety</td><td>Firesafe Co</td><td>September 2023</td></tr>
    <tr><td>Furniture &amp; Fittings</td><td>Routine</td><td>Homestead Reports</td><td>May 2023</td></tr>
    <tr><td>Gymnasium</td><td>Routine</td><td>Homestead Reports</td><td>May 2023</td></tr>
    <tr><td>Hallways</td><td>Routine</td><td>Homestead Reports</td><td>May 2023</td></tr>
    <tr><td>Laundry</td><td>Routine</td><td>Homestead Reports</td><td>May 2023</td></tr>
    <tr><td>Lift</td><td>Liftway</td><td>Routine/Safety</td><td></td></tr>
    <tr><td>Lobby/Recreation Room</td><td>Routine</td><td>Homestead Reports</td><td>May 2023</td></tr>
    <tr><td>Mechanical Ventilation</td><td>Operational</td><td>Airflow FM</td><td></td></tr>
    <tr><td>Pest Management</td><td>Routine</td><td>Homestead Reports</td><td>May 2023</td></tr>
    <tr><td>Recreation Areas</td><td>Routine</td><td>Homestead Reports</td><td>May 2023</td></tr>
    <tr><td>Pool Areas</td><td>Routine</td><td>Homestead Reports</td><td>May 2023</td></tr>
    <tr><td>Roof Access</td><td>Routine</td><td>Homestead Reports</td><td>May 2023</td></tr>
    <tr><td>Sauna</td><td>Routine</td><td>Homestead Reports</td><td>May 2023</td></tr>
    <tr><td>Stairwell</td><td>Routine</td><td>Homestead Reports</td><td>May 2023</td></tr>
    <tr><td>Tennis Court</td><td>Routine</td><td>Homestead Reports</td><td>May 2023</td></tr>
    <tr><td>Washrooms</td><td>Routine</td><td>Homestead Reports</td><td>May 2023</td></tr>
  </table>
  <div class="footer"><span class="num">Page | 5</span>2 Sample Street Canberra City · COPYRIGHT: Homestead Reports</div>
</section>

<!-- ESL summary -->
<section class="page esl">
  <p class="lead">Estimated Service Life (ESL) Summary (indicates estimated service life of the building element and identifies anticipated next major expenditure – other than a routine service/repair)</p>
  <div class="grid-head"><span></span><span>ESL</span><span>2022</span><span>2023</span><span>2024</span><span>2025</span><span>2026</span><span>2027</span><span>2028</span><span>2029</span><span>2030</span><span>2031</span><span>2032</span><span>2033</span><span>2034</span><span>2035</span><span>2036</span><span>2037</span></div>
  <div class="grid-section">SUPERSTRUCTURE</div>
  <div class="grid-row"><span class="lbl">Repaint Building Exterior</span><span class="yrs">10</span><span class="tick" style="grid-column:9"></span></div>
  <div class="grid-row"><span class="lbl">Repaint Soffits</span><span class="yrs">10</span><span class="tick" style="grid-column:9"></span></div>
  <div class="grid-row"><span class="lbl">Repair/Maintain Common Window Coverings</span><span class="yrs">10</span><span class="tick" style="grid-column:7"></span></div>
  <div class="grid-row"><span class="lbl">Repair/Maintain windows</span><span class="yrs">5</span><span class="tick" style="grid-column:7"></span></div>
  <div class="grid-row"><span class="lbl">Maintain Balcony/Patio/Entry Floor Tiles</span><span class="yrs">10</span><span class="tick" style="grid-column:7"></span></div>
  <div class="grid-row"><span class="lbl">Repaint Balustrade &amp; Handrail Fixings</span><span class="yrs">20</span><span class="tick" style="grid-column:13"></span></div>
  <div class="grid-row"><span class="lbl">Repair/Maintain Balcony Membrane</span><span class="yrs">5</span><span class="tick" style="grid-column:5"></span></div>
  <div class="grid-row"><span class="lbl">Repair/Maintain Roof</span><span class="yrs">10</span><span class="tick" style="grid-column:9"></span></div>
  <div class="grid-row"><span class="lbl">Repair/Maintain Skylights</span><span class="yrs">10</span><span class="tick" style="grid-column:5"></span></div>
  <div class="grid-section">BASEMENT/CAR ACCOMODATION</div>
  <div class="grid-row"><span class="lbl">Maintain/Repair Main Garage Door Motor</span><span class="yrs">5</span><span class="tick" style="grid-column:6"></span></div>
  <div class="grid-row"><span class="lbl">Maintain/Repair Main Garage Door Running Gear</span><span class="yrs">5</span><span class="tick" style="grid-column:6"></span></div>
  <div class="grid-row"><span class="lbl">Repaint Door Faces</span><span class="yrs">10</span><span class="tick" style="grid-column:4"></span></div>
  <div class="grid-row"><span class="lbl">Repaint Line Marking</span><span class="yrs">10</span><span class="tick" style="grid-column:7"></span></div>
  <div class="grid-row"><span class="lbl">Replace Basement Exit/Entry Door</span><span class="yrs">40</span><span class="yr-text" style="grid-column:18">2040</span></div>
  <div class="grid-row"><span class="lbl">Service/Replace Storm Water Pumps</span><span class="yrs">5</span><span class="tick" style="grid-column:5"></span></div>
  <div class="grid-row"><span class="lbl">Service/Replace Stormwater Pump Controller</span><span class="yrs">5</span><span class="tick" style="grid-column:4"></span></div>
  <div class="grid-row"><span class="lbl">Clean/Maintain Pump Pits &amp; Enclosures</span><span class="yrs">As Required</span><span class="tick" style="grid-column:4"></span></div>
  <div class="footer"><span class="num">Page | 6</span>2 Sample Street Canberra City · COPYRIGHT: Homestead Reports</div>
</section>

<!-- ACT maintenance plan -->
<section class="page plan">
  <h3>Act maintenance plan</h3>
  <div class="band">INSPECTION TYPES</div>
  <table class="types" style="width:100%;border-collapse:collapse;margin-bottom:8px">
    <tr><td>ROUTINE</td><td>General inspection to determine that the building element is in acceptable order showing no signs of deterioration or damage that may require attention or repair</td></tr>
    <tr><td>ROUTINE/SAFETY</td><td>Following the guidelines of a routine inspection with a particular focus on items that may cause injury to owners/occupants/visitors</td></tr>
    <tr><td>SERVICE</td><td>An inspection where some additional level of attention or maintenance may be required, e.g. cleaning a pool filter</td></tr>
    <tr><td>OPERATIONAL</td><td>Inspection to ascertain the element is operational</td></tr>
    <tr><td>COMPLIANCE</td><td>Inspect, test and maintain as required to ensure that the building element meets a particular Regulation or Standard</td></tr>
    <tr><td>SANITATION</td><td>Required Health &amp; Safety check for residents</td></tr>
  </table>
  <div class="h-blue" style="font-size:3.6px">SUPERSTRUCTURE</div>
  <div class="meta"><span><b>Inspector:</b> Homestead Reports</span><span><b>Inspection Type:</b> Routine</span><span><b>Frequency:</b> Annual</span><span><b>Last Inspection Date:</b> 2/5/2022</span></div>
  <div class="nextdate">Next Inspection Date: 2/5/2023</div>
  <div class="band teal">BUILDING WATERPROOFING</div>
  <div class="wp-row"><span class="lab">Estimated Service Lifespan</span><span class="y">2022</span><span class="y">2023</span><span class="y">2024</span><span class="y">2025</span><span class="y">2026</span><span class="y">2027</span><span class="y">2028</span><span class="y">2029</span><span class="y">2030</span><span class="y">2031</span><span class="y">2032</span><span class="y">2033</span><span class="y">2034</span><span class="y">2035</span><span class="y">2036</span><span class="y">2037</span></div>
  <div class="wp-note">Forecast date where major refurbishment or replacement may be required for each particular asset or capital item. Where a Sinking Fund has been prepared, this information may represent forecasted expenditure.</div>
  <div class="wp-row" style="border-bottom:.4px solid var(--ink);padding-bottom:1px"><span class="lab" style="color:#e45c4a;font-weight:400">5 years</span><span style="width:152px"></span><svg width="4" height="4" viewBox="0 0 4 4"><rect x=".2" y=".2" width="3.6" height="3.6" fill="none" stroke="var(--teal)" stroke-width=".4"/><path d="M.9 2 L1.7 2.9 L3.2 1" fill="none" stroke="var(--teal)" stroke-width=".4"/></svg></div>
  <div style="font-size:2.6px;font-style:italic;font-weight:600;margin:2px 0">Service/Routine Inspection History</div>
  <table class="history" style="width:100%;border-collapse:collapse">
    <tr class="head"><td>Date</td><td>Company</td><td>Type</td><td>Cost</td><td>Details</td></tr>
    <tr><td><b>2017</b></td><td>Unknown</td><td>Waterproofing repairs</td><td>$41,659</td><td>Identified in Sinking Fund (prepared July 18 2017)</td></tr>
  </table>
  <div class="footer"><span class="num">Page | 12</span>2 Sample Street Canberra City · COPYRIGHT: Homestead Reports</div>
</section>

<!-- Scope & limitations -->
<section class="page scope">
  <h3>COPE &amp; LIMITATIONS OF INSPECTION &amp; MAINTENANCE PLAN</h3>
  <p><span class="h-teal" style="font-weight:400;font-style:italic">Manner of Inspection:</span> visual only in normal lighting.</p>
  <h4>REPORT PURPOSE</h4>
  <p>The purpose of this report is to collate a comprehensive data file on the building as it exists on the day of inspection. A Maintenance Plan is designed to provide the Management Group with a road map that identifies common areas of the building that must be monitored and maintained by the Owners Corporation. Areas included will comprise elements such as structures, equipment, fittings, furniture, security access, fire protection, fencing, gates, common area painting and pool safety.</p>
  <h4>IMPORTANT – THIS IS NOT A COMPREHENSIVE CONDITION OR DEFECT REPORT</h4>
  <p>This is not a comprehensive defect report. It is critical to understand that our inspectors are not experts on many of the building elements that form part of this plan and that our inspection was undertaken to create a datafile that will be subsequently used by external expert service providers during routine and safety inspections.</p>
  <p>Any comments or observations made regarding defects or the condition of a building element are noted in this report as a courtesy. We are not required to report on defects and cannot guarantee or take responsibility for any or all defects that have or have not been identified.</p>
  <h4>THIS MAINTENANCE PLAN REQUIRES REVIEW PRIOR TO CIRCULATION</h4>
  <p>Prior to circulation of this report, it is the responsibility of the Strata Management Group and the Executive Committee to review the plan and ensure all common area elements have been identified. Common area elements vary from building to building; in most cases our inspection is undertaken without the escort of a Building Manager. It is therefore dependent on the documentation that has been supplied to us and our own discretion to determine elements on the block that should be appropriately included.</p>
  <h4>REFERENCE TO STANDARDS</h4>
  <p>Where Australian (or other) Standards have been referenced, these are subject to change or update and are simply used as a guide for the reader. When building elements are inspected and maintained by the industry expert during routine and safety inspections, they will subsequently confirm adherence to the relevant Standard.</p>
  <h4>ESTIMATED SERVICE LIFESPAN</h4>
  <p>We have arrived at Estimated Service Lifespans referenced in this document via industry research, expert building opinions, trade manuals, Australian Standards and experience. Our observations regarding the lifespan of a building element is subjective and in no way guarantees that the lifespan noted on the maintenance plan is definitive or without subject to change. We cannot guarantee that the estimated year for capital expenditure is accurate and will be subject to change.</p>
  <h4>INSPECTION FREQUENCY</h4>
  <p>We have arrived at estimated inspection frequency based via industry research, expert building opinions, trade manuals, Australian Standards and experience. Our recommended inspection frequency should be cross referenced with the expert service provider for a particular building element and the expert technician's advice should always be adhered to even if contrary to this document.</p>
  <h4>NEXT INSPECTION DATE</h4>
  <p>We work with the Strata Manager to estimate the next inspection date for each building element identified in this report. The date may be based on a past inspection or we may provide a limited opinion on the next due date based on our observations on the day.</p>
  <div class="footer"><span class="num">Page | 15</span>2 Sample Street Canberra City · COPYRIGHT: Homestead Reports</div>
</section>

<!-- Access & safety -->
<section class="page terms">
  <p>where fire, pool and mechanical safety are of concern, the next date of inspection should be updated by the Strata Manager based on the most relevant past inspection on file.</p>
  <h4>TESTING</h4>
  <p>If our inspector has tested a building element during the preparation of this maintenance plan and subsequently made comment, we confirm that this is not a comprehensive test by an industry expert and should not replace the attendance of an appropriately qualified technician to determine the condition of the element. We cannot guarantee or take responsibility for any or all defects that have or have not been identified.</p>
  <h3>SAFETY &amp; REASONABLE ACCESS</h3>
  <p>Australian Standard 4349.1 – 2007 3.2.2 The extent of accessible areas shall be determined by the inspector at the time of inspection, based on the conditions encountered at the time of inspection. The inspector shall also determine whether sufficient space is available to allow safe access. The inspection shall include only accessible areas and areas that are within the inspector's line of sight and close enough to enable reasonable appraisal. Reasonable access does not include removing screws and bolts to access covers.</p>
  <p style="font-style:italic">Reasonable access is determined in accordance with the provisions of the following WHS requirements</p>
  <table class="access">
    <tr><th>Area</th><th>Access Manhole MM</th><th>Crawl Space MM</th><th>Height</th></tr>
    <tr><td>Subfloor</td><td>500 x 400</td><td>Vertical clearance - Timber Floor: 400* Concrete Floor: 500</td><td></td></tr>
    <tr><td>Roof Interior</td><td>400 x 500</td><td>600 x 600</td><td>Accessible from a 3.6 m ladder</td></tr>
    <tr><td>Roof Exterior</td><td></td><td></td><td>Accessible from a 3.6 m ladder</td></tr>
  </table>
  <p style="font-style:italic">* To underside of bearer, joist or other obstruction to access.</p>
  <p><span class="h-teal" style="font-weight:500">Roof Cover Inspection</span> - Work Health and Safety requirements determine that an inspector accessing a roof cover must be protected by harnessed safety lines and or edge protection. These safety measures are not practical during a presale inspection, therefore this report is restricted to a "top-of-ladder" inspection. This report is not a guarantee that defects do not exist in any part of the property not specifically seen and described by the inspector.</p>
  <p><span class="h-teal" style="font-weight:500">Ceiling Cavity Inspection</span> - Work Health and Safety requirements determine that an inspector entering a ceiling cavity must have direct access to properly constructed walkways to eliminate the possibility of falling through the ceiling lining. Generally, walkways are limited in a ceiling cavity so invariably sections of the roof structure will be inspected from a distance with limited access and often an impaired line-of-sight.</p>
  <p>Safety requirements prevent the inspector from traversing a ceiling cavity where safety elements are not available. This report is not a guarantee that defects do not exist in inaccessible areas.</p>
  <p><span class="h-teal" style="font-weight:500">Work Health and Safety Act 2011</span> - A non-residential building and the common property of some group residential buildings will fall within the definition of a workplace for the purposes of the Work Health and Safety Act 2011.</p>
  <p style="margin-bottom:0">The owners of workplaces must ensure that:</p>
  <ul><li>premises are safe and without risk</li><li>plant and substances are used without risk</li><li>workers are trained in WHS, are aware of their obligations and act in a safe manner</li></ul>
  <div class="footer"><span class="num">Page | 16</span>2 Sample Street Canberra City · COPYRIGHT: Homestead Reports</div>
</section>

</body>
</html>
```